Thornbury Lettings Managment Ltd website

Need a website To inform people/clients of the services we provide. 5 pages total with a local feel. Bristol, UK. I have logo artwork already is like the look based on
incorporate the artwork attached for theme, feel and colours fonts info etc

To best describe the business have a brief look at www.fernwickhomes.example.co.uk which is a local firm offering the same services. This is for your ref only and not to be copied.

Target Market(s)

Property Investors/Landlords

Coding

Coded - Design and coding required

Number of Pages Required

5+ page

Colors
0392cd
f68d4d

Requirements
Must have
• local feel. Possibly using some local architecture or historic landmarks etc. This is fexible.
• most also be mobile device compatible
Nice to have
• the membership logos - files attached: KTB, DWF, GMV and safehold-example.co.uk

```html
<!DOCTYPE html>
<html lang="en">
<head>
<meta charset="utf-8">
<title>Thornbury Lettings Managment Ltd</title>
<link href="https://fonts.googleapis.com/css2?family=Noto+Serif:wght@400;700&family=Open+Sans:wght@400;600;700&display=swap" rel="stylesheet">
<style>
  :root {
    --orange: #e8a23b;
    --navy: #27306b;
    --ink: #1c1c1c;
    --white: #ffffff;
    --rule: #dcdcdc;
    --muted: #8a8a8a;
    --footer: #0e0e0e;
  }
  * { margin: 0; padding: 0; box-sizing: border-box; }
  html, body { width: 779px; height: 1200px; overflow: hidden; }
  body { position: relative; background: var(--white); font-family: "Open Sans", sans-serif; color: var(--ink); }

  .brand { position: absolute; display: flex; align-items: center; gap: 6px; color: var(--white); font-family: "Noto Serif", serif; font-weight: 700; }
  .brand-mark { width: 10px; height: 10px; background: var(--white); }

  .nav { position: absolute; display: flex; gap: 30px; list-style: none; font-size: 8px; font-weight: 700; letter-spacing: 0.6px; color: var(--white); }
  .nav .active { border-bottom: 2px solid var(--orange); padding-bottom: 3px; }

  /* Hero */
  .hero { position: absolute; left: 0; top: 0; width: 779px; height: 403px; }
  .hero-photo { position: absolute; inset: 0;
    background: radial-gradient(ellipse at 60% 78%, rgba(205,140,90,0.55) 0%, rgba(90,70,80,0.2) 35%, transparent 60%),
                linear-gradient(180deg, #2a3140 0%, #3a4252 45%, #4c4a52 70%, #1d1d22 100%); }
  .hero-monument { position: absolute; left: 0; top: 60px; width: 200px; height: 343px;
    background: linear-gradient(180deg, rgba(10,10,14,0.75), rgba(10,10,14,0.95)); }
  .hero .brand { left: 160px; top: 8px; font-size: 12px; }
  .hero .nav { right: 152px; top: 12px; }
  .hero-title { position: absolute; left: 0; width: 779px; text-align: center; top: 134px; font-family: "Noto Serif", serif; font-size: 50px; letter-spacing: 5px; color: var(--orange); font-weight: 400; }
  .hero-sub { position: absolute; left: 0; width: 779px; text-align: center; top: 196px; font-family: "Noto Serif", serif; font-size: 23px; letter-spacing: 1.5px; color: var(--white); }
  .hero-btn { position: absolute; left: 371px; top: 240px; width: 38px; padding-bottom: 3px; border-bottom: 1px solid var(--white); text-align: center; font-size: 5px; font-weight: 700; letter-spacing: 0.5px; color: var(--white); }

  /* Services */
  .services { position: absolute; left: 0; top: 403px; width: 779px; height: 337px; }
  .section-title { position: absolute; left: 0; width: 779px; top: 44px; text-align: center; font-size: 9px; font-weight: 700; letter-spacing: 1px; }
  .services-stem { position: absolute; left: 389px; top: 62px; width: 1px; height: 55px; background: var(--rule); }
  .services-grid { position: absolute; left: 150px; top: 117px; width: 474px; height: 170px; border: 1px solid var(--rule); }
  .services-grid::after { content: ""; position: absolute; left: 239px; top: 0; width: 1px; height: 100%; background: var(--rule); }
  .service-photo { position: absolute; top: 26px; height: 116px; }
  .service-photo.tenants { left: 32px; width: 168px; background: linear-gradient(180deg, #9fb4c9 0%, #c3c9cf 40%, #8a8578 70%, #5e5a52 100%); }
  .service-photo.landlords { left: 270px; width: 166px; background: radial-gradient(ellipse at 50% 50%, #8f9a6e 0%, #6f7a55 45%, #525a44 100%); }
  .service-label { position: absolute; font-size: 10px; font-weight: 700; letter-spacing: 1.4px; color: var(--orange); line-height: 1.35; }
  .service-label.landlords { left: 600px; top: 90px; text-align: right; }
  .service-label.tenants { left: 152px; top: 276px; }

  /* Stats */
  .stats { position: absolute; left: 0; top: 740px; width: 779px; height: 143px; border-top: 1px solid var(--rule); }
  .stat { position: absolute; top: 46px; display: flex; align-items: center; gap: 12px; }
  .stat-rule { width: 34px; height: 1px; background: var(--navy); }
  .stat-number { font-family: "Noto Serif", serif; font-size: 50px; color: var(--navy); line-height: 1; }
  .stat-label { font-family: "Noto Serif", serif; font-size: 13px; letter-spacing: 1.5px; color: var(--orange); line-height: 1.3; }
  .stat.years { left: 150px; }
  .stat.customers { left: 400px; }

  /* About */
  .about { position: absolute; left: 0; top: 883px; width: 779px; height: 287px; }
  .about-photo { position: absolute; inset: 0;
    background: linear-gradient(180deg, rgba(20,18,16,0.82), rgba(20,18,16,0.9)),
                radial-gradient(ellipse at 40% 50%, #6b6455 0%, #3b372f 70%); }
  .about .brand { left: 160px; top: 108px; font-size: 34px; color: rgba(255,255,255,0.78); font-weight: 400; gap: 12px; }
  .about .brand-mark { width: 26px; height: 26px; background: rgba(255,255,255,0.78); }
  .about-title { position: absolute; left: 444px; top: 78px; font-size: 10px; font-weight: 700; letter-spacing: 1px; color: var(--orange); }
  .about-text { position: absolute; left: 444px; top: 96px; width: 170px; font-size: 7px; line-height: 1.5; color: #cfcfcf; }
  .about-btn { position: absolute; left: 462px; top: 196px; padding-bottom: 3px; border-bottom: 1px solid var(--white); font-size: 6px; font-weight: 700; letter-spacing: 0.6px; color: var(--white); }

  /* Footer */
  .footer { position: absolute; left: 0; top: 1170px; width: 779px; height: 30px; background: var(--footer); }
  .footer .brand { left: 160px; top: 8px; font-size: 10px; }
  .footer .brand-mark { width: 8px; height: 8px; }
  .footer .nav { right: 152px; top: 11px; font-size: 7px; gap: 24px; }
</style>
</head>
<body>

<header class="hero">
  <div class="hero-photo" role="img" aria-label="Dusk photograph over the city skyline with a historic columned monument in the foreground"></div>
  <div class="hero-monument" role="img" aria-label="Silhouette of the historic monument"></div>
  <div class="brand"><span class="brand-mark"></span>Thornbury</div>
  <ul class="nav">
    <li class="active">HOME</li><li>LANDLORDS</li><li>TENANTS</li><li>ABOUT US</li><li>CONTACT</li>
  </ul>
  <h1 class="hero-title">THORNBURY</h1>
  <p class="hero-sub">lettings managment ltd</p>
  <div class="hero-btn">DISCOVER</div>
</header>

<section class="services">
  <h2 class="section-title">OUR SERVICES</h2>
  <div class="services-stem"></div>
  <div class="services-grid">
    <div class="service-photo tenants" role="img" aria-label="Photograph of a historic city street and square"></div>
    <div class="service-photo landlords" role="img" aria-label="Aerial photograph of the city centre and parkland"></div>
  </div>
  <div class="service-label landlords">FOR<br>LANDLORDS</div>
  <div class="service-label tenants">FOR TENANTS</div>
</section>

<section class="stats">
  <div class="stat years">
    <span class="stat-rule"></span>
    <span class="stat-number">15</span>
    <span class="stat-label">YEARS<br>OF EXPERIENCE</span>
  </div>
  <div class="stat customers">
    <span class="stat-rule"></span>
    <span class="stat-number">450</span>
    <span class="stat-label">LOYAL<br>CUSTOMERS</span>
  </div>
</section>

<section class="about">
  <div class="about-photo" role="img" aria-label="Darkened aerial photograph of the city"></div>
  <div class="brand"><span class="brand-mark"></span>Thornbury</div>
  <h2 class="about-title">ABOUT US</h2>
  <p class="about-text">Thornbury is a local letting and management firm caring for homes across the city. We look after landlords and tenants alike, handling every detail from first viewing to final inspection with honest, friendly and reliable service.</p>
  <div class="about-btn">LEARN MORE</div>
</section>

<footer class="footer">
  <div class="brand"><span class="brand-mark"></span>Thornbury</div>
  <ul class="nav">
    <li>HOME</li><li>LANDLORDS</li><li>TENANTS</li><li>ABOUT US</li><li>CONTACT</li>
  </ul>
</footer>

</body>
</html>
```